New Podcast, Ridgewater Wellness Bureaus

We need a cover design for a new podcast that we are producing.

Title: Ridgewater Wellness Bureaus

This is a business podcast for Native American tribal organizations, representing indigenous peoples of the United States.

Pull colors from the logo.
Do not add photos of people into the design.

Public Health, Statistics, Epidemiology, Tribal Organizations, NonProfits

```html
<!DOCTYPE html>
<html lang="en">
<head>
<meta charset="utf-8">
<title>Ridgewater Wellness Bureaus Podcast Cover</title>
<link href="https://fonts.googleapis.com/css2?family=League+Gothic&family=Oswald:wght@400;500&family=Great+Vibes&family=Montserrat:wght@800&display=swap" rel="stylesheet">
<style>
  :root {
    --teal-light: #0a9c9d;
    --teal-mid: #087c85;
    --teal-dark: #0a566a;
    --orange: #c8692a;
    --logo-teal: #0f5f70;
    --white: #ffffff;
    --pattern-red: #b8323a;
    --pattern-gold: #e2a84a;
  }
  html, body {
    margin: 0;
    padding: 0;
    width: 1200px;
    height: 1200px;
    overflow: hidden;
  }
  .cover {
    position: relative;
    width: 1200px;
    height: 1200px;
    overflow: hidden;
    background: radial-gradient(circle at 30% 25%, var(--teal-light) 0%, var(--teal-mid) 45%, var(--teal-dark) 100%);
    color: var(--white);
  }
  .client-mark {
    position: absolute;
    left: 106px;
    top: 78px;
    width: 383px;
    height: 154px;
    background: var(--white);
    display: flex;
    align-items: center;
    gap: 18px;
    padding: 0 24px;
    box-sizing: border-box;
  }
  .client-mark .dot {
    flex: none;
    width: 96px;
    height: 96px;
    border-radius: 50%;
    background: var(--orange);
  }
  .client-mark .name {
    font-family: "Montserrat", sans-serif;
    font-weight: 800;
    font-size: 24px;
    line-height: 1.1;
    color: var(--logo-teal);
    text-transform: uppercase;
  }
  .social {
    position: absolute;
    top: 78px;
    right: 49px;
    display: flex;
    gap: 7px;
  }
  .social span {
    width: 38px;
    height: 38px;
    border-radius: 50%;
    background: var(--white);
  }
  .kicker {
    position: absolute;
    left: 114px;
    top: 246px;
    font-family: "Oswald", sans-serif;
    font-weight: 500;
    line-height: 1;
    transform: scaleY(1.25);
    transform-origin: left bottom;
  }
  .kicker .small { font-size: 48px; }
  .kicker .large { font-size: 68px; }
  .title {
    position: absolute;
    left: 104px;
    top: 322px;
    margin: 0;
    font-family: "League Gothic", sans-serif;
    font-weight: 400;
    font-size: 248px;
    line-height: 200px;
    letter-spacing: 1px;
    text-transform: uppercase;
  }
  .title span { display: block; }
  .host {
    position: absolute;
    left: 120px;
    top: 952px;
    width: 210px;
    text-align: center;
  }
  .script {
    font-family: "Great Vibes", cursive;
    font-size: 46px;
    line-height: 1;
  }
  .host .person {
    font-family: "Oswald", sans-serif;
    font-weight: 500;
    font-size: 66px;
    line-height: 1;
    transform: skewX(-8deg) scaleX(0.85);
    letter-spacing: -1px;
  }
  .divider {
    position: absolute;
    left: 354px;
    top: 972px;
    width: 2px;
    height: 112px;
    background: rgba(255,255,255,0.6);
  }
  .stream {
    position: absolute;
    left: 372px;
    top: 962px;
    width: 220px;
  }
  .stream .live {
    font-family: "Oswald", sans-serif;
    font-weight: 500;
    font-size: 52px;
    line-height: 1;
    transform: skewX(-10deg) scaleX(0.8);
    transform-origin: left;
    display: inline-block;
  }
  .stream .script {
    position: absolute;
    left: 78px;
    top: 4px;
    font-size: 44px;
  }
  .stream .word {
    display: block;
    font-family: "Oswald", sans-serif;
    font-weight: 500;
    font-size: 76px;
    line-height: 0.9;
    transform: skewX(-10deg) scaleX(0.78);
    transform-origin: left;
  }
  .studio {
    position: absolute;
    left: 882px;
    top: 880px;
    width: 262px;
    display: flex;
    flex-direction: column;
    align-items: center;
    gap: 18px;
  }
  .studio .dot {
    width: 104px;
    height: 104px;
    border-radius: 50%;
    background: var(--orange);
  }
  .studio .name {
    font-family: "Montserrat", sans-serif;
    font-weight: 800;
    font-size: 30px;
    line-height: 1.15;
    text-align: center;
    text-transform: uppercase;
    letter-spacing: 2px;
  }
  .pattern-band {
    position: absolute;
    left: 0;
    bottom: 0;
    width: 1200px;
    height: 86px;
    background: linear-gradient(90deg, var(--pattern-red), var(--teal-light) 30%, var(--pattern-gold) 55%, var(--teal-light) 75%, var(--pattern-red));
  }
</style>
</head>
<body>
<main class="cover">
  <div class="client-mark">
    <span class="dot"></span>
    <span class="name">Ridgewater Wellness Bureaus</span>
  </div>

  <div class="social" aria-hidden="true">
    <span></span><span></span><span></span><span></span>
  </div>

  <div class="kicker"><span class="small">present</span> <span class="large">podcast on</span></div>

  <h1 class="title">
    <span>Ridgewater</span>
    <span>Wellness</span>
    <span>Bureaus</span>
  </h1>

  <div class="host">
    <div class="script">Hosted By</div>
    <div class="person">Mr.Hale</div>
  </div>

  <div class="divider"></div>

  <div class="stream">
    <span class="live">Live</span>
    <span class="script">Stream</span>
    <span class="word">podcast</span>
  </div>

  <div class="studio">
    <span class="dot"></span>
    <span class="name">Harbor<br>Podcast Studio</span>
  </div>

  <div class="pattern-band" role="img" aria-label="Geometric Native-inspired triangle and chevron border pattern in teal, red, gold and white"></div>
</main>
</body>
</html>
```